Website Design for Solar Panel Company

We are working with a company called BrightVX.

Some sites to use for content/competitors and inspiration:
https://www.dawnmill.com
https://prod.cdn-prod.raylokt.com
https://mossbeamvolt.net
https://www.quorvin.com/solarpanels

Thank you for taking the time to consider designing a website for us. We are web developers based in Stockton, CA, USA. Most of our projects go through the same process. Understanding this process may help you win a project with us. We custom-code all of our websites in-house. We don’t have any requirements as to what tools you use for your design, but we prefer Figma files. For any design that we label as four-stars, we send it to the client for review. The client picks the final design they want us to use. Once we complete this process, we will continue to show additional clients all the four-star sites and purchase them later. Your designs will have multiple chances to sell. For better chances of success, we ask that you follow these guidelines.

IMAGES:
If you use any images or icons in the design, we ask that you have a link to the asset so we can purchase the image/icon. Most of the designs we submit do not have the customer’s images on them unless they have some great images. Be creative; show us the feeling you are trying to portray with your image choices. Use any royalty-free site you choose. We subscribe to Corvane and mainly use their images, but we can purchase images outside of Corvane. PLEASE NOTE: we will not submit designs to clients with watermarks on the images.

FONTS:
We ask that you identify the fonts used in the design. This can be done in a message if you want. We typically use Tivelo Fonts and Corvane Fonts.

CONTENT:
We're always open to different content and ideas. We often submit designs with stock images so the client can see our vision. We typically take pictures after the website launch to use their images with our vision. Lorem Ipsum is fine for paragraphs, but we ask that you write the headers in correct English. We want to be able to show the vision and identify the sections of the website.

INSPIRATION:
We typically add a couple of links in the brief of websites we like to help you get started in your design.

REVISIONS:
We do not often ask for revisions of the designs unless we see something in the design that may not appeal to the client. If there are slight changes that we want to make, we do that in the development process.

FEEDBACK:
We rarely give feedback on designs during the design process. We are working on many website projects and do not have the time to provide feedback. We usually respond if your request is well thought out and asks specific questions, but a note asking “feedback, please” usually goes unanswered.

```html
<!DOCTYPE html>
<html lang="en">
<head>
<meta charset="utf-8">
<title>BrightVX – Renewable Energy Website</title>
<link href="https://fonts.googleapis.com/css2?family=Outfit:wght@300;400;500;600&display=swap" rel="stylesheet">
<style>
:root{
  --stage:#000;
  --green:#2a9a0a;
  --green-soft:#7ab85f;
  --mint:#e7fadb;
  --mint-2:#eefde4;
  --ink:#1c1c1c;
  --muted:#6b6b6b;
  --grey:#f4f4f4;
  --lav:#efeafb;
  --lav-2:#f7f5fc;
  --footer:#1b1b1b;
  --white:#fff;
}
*{margin:0;padding:0;box-sizing:border-box}
html,body{width:1200px;height:1200px;overflow:hidden;background:var(--stage)}
body{font-family:"Outfit",sans-serif;color:var(--ink);position:relative}
.page{position:absolute;width:432px;overflow:hidden;background:var(--grey)}
.page-left{left:89px;top:60px;height:1140px}
.page-right{left:600px;top:0;height:1200px}
.abs{position:absolute}
.brand{font-weight:600;font-size:12px;letter-spacing:.5px;color:var(--ink)}
.btn{position:absolute;display:flex;align-items:center;justify-content:center;border-radius:20px;background:var(--green);color:#fff;font-weight:500}
.btn-outline{background:transparent;border:1px solid var(--green);color:var(--green)}
.center{text-align:center}
p{line-height:1.55}

/* hero */
.hero-photo{position:absolute;left:0;top:0;width:432px;height:317px;background:linear-gradient(160deg,#5f8fd6 0%,#3c64b8 45%,#27407c 70%,#9bb2c9 100%)}
.nav{position:absolute;top:14px;left:193px;display:flex;gap:8px;font-size:4.5px;color:#fff}
.nav .active{font-weight:600}
.hero-title{position:absolute;top:44px;left:0;width:432px;font-size:20px;line-height:23px;font-weight:500;color:#fff}
.hero-text{position:absolute;top:96px;left:100px;width:232px;font-size:6px;font-weight:300;color:#fff}
.feature{position:absolute;top:242px;width:110px;text-align:center}
.feature h3{font-size:7px;font-weight:500;color:var(--green);margin-top:6px}
.feature p{font-size:4.6px;color:var(--muted);margin-top:6px;line-height:1.75}
.divider{position:absolute;top:262px;width:1px;height:37px;background:var(--green)}

/* about */
.about-photo{position:absolute;left:135px;top:317px;width:297px;height:198px;background:linear-gradient(170deg,#8aa0b7 0%,#6d83a0 35%,#3f4f6e 60%,#9fb17a 100%);clip-path:polygon(0 0,100% 0,100% 100%,45% 100%)}
.eyebrow{font-size:5.5px;letter-spacing:.3px}
.section-title{font-size:15px;font-weight:500;line-height:19.2px}
.body-s{font-size:6px;color:#333}

/* services */
.card{position:absolute;top:586px;width:114px;height:178px;background:#fff;border-radius:6px;overflow:hidden}
.card .ph{height:96px}
.card h4{font-size:7px;font-weight:500;margin:6px 7px 0}
.card p{font-size:4.6px;color:#444;margin:3px 7px 0;line-height:1.6}
.card .more{display:flex;align-items:center;gap:3px;font-size:4.6px;color:var(--green);margin:5px 10px 0}

/* contact */
.contact-band{position:absolute;left:0;width:432px;background:linear-gradient(180deg,#f4f4f4 0%,#c9d9bf 35%,#7ab85f 100%)}
.form-card{position:absolute;background:#fff;border-radius:8px}
.form-card h4{font-size:10px;font-weight:500}
.label{font-size:4.5px;margin-bottom:3px}
.field{border:.6px solid #444;height:15px;margin-bottom:8px}
.field.msg{height:54px;font-size:4px;color:#888;padding:4px}
.check{display:flex;align-items:center;gap:3px;font-size:4px}
.check i{width:6px;height:6px;border:.6px solid #444;display:inline-block}
.check u{color:var(--ink)}
.submit{width:31px;height:14px;background:#111;color:#fff;border-radius:10px;font-size:4.5px;display:flex;align-items:center;justify-content:center;margin-top:10px}
.contact-line{position:absolute;display:flex;align-items:center;gap:7px;font-size:7px}

/* why */
.why-photo{position:absolute;left:21px;top:245px;width:168px;height:143px;background:radial-gradient(ellipse at 50% 40%,#5f8a3a 0%,#8f6b48 45%,rgba(244,244,244,0) 70%)}
.tick-list{position:absolute;left:222px;top:311px;list-style:none;font-size:7.2px;color:#555}
.tick-list li{display:flex;align-items:flex-start;gap:5px;margin-bottom:4.5px;line-height:13px}
.tick-list svg{flex:none;margin-top:2px}

/* testimonials */
.tcard{position:absolute;top:533px;width:175px;height:81px;background:#fff;border-radius:3px;padding:10px 7px 0}
.tcard p{font-size:5px;line-height:8.3px}
.tcard.active{background:var(--green);color:#fff}
.who{position:absolute;top:48px;left:7px;display:flex;align-items:center;gap:6px}
.avatar{width:19px;height:19px;border-radius:50%;background:#8a7362}
.who b{display:block;font-size:7px;font-weight:500}
.who span{font-size:5px}
.stars{position:absolute;top:52px;left:106px;width:55px;height:12px;border-radius:8px;background:#fff;display:flex;align-items:center;justify-content:center;gap:2px}

/* faq */
.faq{position:absolute;left:39px;width:353px;display:flex;padding:0 18px}
.faq .num{font-size:15px;color:#888;width:32px;flex:none}
.faq h5{font-size:10px;font-weight:500;line-height:11.5px;flex:1;padding-right:14px}
.faq .tog{width:13px;height:13px;border-radius:50%;background:#fff;font-size:6px;display:flex;align-items:center;justify-content:center;flex:none}

/* footer */
.footer{position:absolute;left:0;top:1066px;width:432px;height:134px;background:var(--footer);color:#fff}
.fcol{position:absolute;top:21px}
.fcol h6{font-size:5.5px;font-weight:400;letter-spacing:.3px;margin-bottom:6px}
.fcol li{list-style:none;font-size:3.6px;margin-bottom:4.4px;display:flex;align-items:center;gap:3px}
.fcol li i{width:4px;height:4px;background:#fff;display:inline-block;border-radius:1px}
</style>
</head>
<body>

<!-- ============ LEFT PAGE ============ -->
<section class="page page-left">
  <div class="hero-photo" role="img" aria-label="Photo of a worker in a hard hat inspecting rooftop solar panels under a blue sky"></div>
  <svg class="abs" style="left:0;top:0" width="432" height="317" viewBox="0 0 432 317">
    <path d="M432 83 C400 95 370 110 346 126 C320 150 305 175 284 188 C240 215 200 235 160 232 C100 230 40 200 0 213 L0 317 L432 317 Z" fill="var(--mint)"/>
    <circle cx="94" cy="205" r="4" fill="#e8e8e8"/>
  </svg>

  <div class="brand abs" style="left:70px;top:11px">BrightVX</div>
  <nav class="nav"><span class="active">Home</span><span>About Us</span><span>Services</span><span>Products</span><span>Contact</span></nav>
  <div class="btn" style="left:322px;top:10px;width:42px;height:12px;font-size:4.5px">Get Started</div>

  <h1 class="hero-title center">Power Your Life with<br>Sustainable Energy</h1>
  <p class="hero-text center">Lorem ipsum dolor sit amet consectetur. Quam urna elit tellus id. Fringilla donec non tincidunt lobortis montes neque. Ultricies laoreet integer sem morbi nibh fames lobortis. Nulla lorem felis nibh a.</p>
  <div class="btn" style="left:173px;top:133px;width:84px;height:17px;font-size:6px">Discover Our Services</div>

  <div class="feature" style="left:38px">
    <svg width="16" height="18" viewBox="0 0 16 18" fill="none" stroke="var(--green)" stroke-width="1"><path d="M8 8V18M8 8L8 1M8 8L1.5 12M8 8L14.5 12"/></svg>
    <h3>Reliable Renewable Energy</h3>
    <p>We provide reliable and efficient renewable energy solutions tailored to meet your specific needs.</p>
  </div>
  <div class="divider" style="left:156px"></div>
  <div class="feature" style="left:159px">
    <svg width="18" height="18" viewBox="0 0 18 18" fill="none" stroke="var(--green)" stroke-width="1.2"><circle cx="9" cy="8" r="4"/><path d="M7 13h4M7.5 15.5h3M9 1v1.5M2 8h1.5M14.5 8H16M4 3l1 1M14 3l-1 1"/></svg>
    <h3>Expertise and Innovation</h3>
    <p>With our extensive expertise and innovative technologies, we are at the forefront of the renewable energy industry.</p>
  </div>
  <div class="divider" style="left:271px"></div>
  <div class="feature" style="left:280px">
    <svg width="16" height="18" viewBox="0 0 16 18" fill="none" stroke="var(--green)" stroke-width="1.3"><path d="M2 11V8a6 6 0 0112 0v3"/><rect x="1.5" y="10" width="3" height="5" rx="1"/><rect x="11.5" y="10" width="3" height="5" rx="1"/></svg>
    <h3>Exceptional Customer Service</h3>
    <p>At BrightVX, customer satisfaction is our top priority. Our team of dedicated professionals is committed to providing exceptional service</p>
  </div>

  <div class="about-photo" role="img" aria-label="Photo of a house roof covered with solar panels, mountains and green fields behind"></div>
  <div class="eyebrow abs" style="left:7px;top:334px">ABOUT US</div>
  <h2 class="section-title abs" style="left:7px;top:346px;width:140px">Empowering a Sustainable Future with Innovative Energy Solutions</h2>
  <p class="body-s abs" style="left:7px;top:427px;width:135px">Lorem ipsum dolor sit amet consectetur. Quam urna elit tellus id. Fringilla donec non tincidunt lobortis montes neque. Ultricies laoreet integer sem morbi nibh fames lobortis. Nulla lorem felis nibh a.</p>
  <div class="btn" style="left:7px;top:485px;width:46px;height:15px;font-size:4.5px">Learn More</div>

  <h2 class="section-title abs center" style="left:0;top:553px;width:432px">Services we provide</h2>

  <article class="card" style="left:37px">
    <div class="ph" role="img" aria-label="Photo of solar panel arrays on a green field" style="background:linear-gradient(180deg,#8fa3d8 0%,#4a5fa8 55%,#7f9b3a 100%)"></div>
    <h4>Solar Energy Solutions</h4>
    <p>Lorem ipsum dolor sit amet consectetur. Tortor nec sed duis tristique ante massa neque. Eget lacus est volutpat velit quam cursus non enim. Elementum tempus ultrices cursus risus sit.</p>
    <div class="more">Learn More <svg width="7" height="5" viewBox="0 0 7 5" fill="none" stroke="var(--green)" stroke-width=".7"><path d="M0 2.5h6M4 .5l2 2-2 2"/></svg></div>
  </article>
  <article class="card" style="left:159px">
    <div class="ph" role="img" aria-label="Photo of two engineers in safety vests looking at wind turbines" style="background:linear-gradient(180deg,#d9dcde 0%,#b9bec2 60%,#c7cf4a 100%)"></div>
    <h4>Wind Energy Solutions</h4>
    <p>Lorem ipsum dolor sit amet consectetur. Tortor nec sed duis tristique ante massa neque. Eget lacus est volutpat velit quam cursus non enim. Elementum tempus ultrices cursus risus sit.</p>
    <div class="more">Learn More <svg width="7" height="5" viewBox="0 0 7 5" fill="none" stroke="var(--green)" stroke-width=".7"><path d="M0 2.5h6M4 .5l2 2-2 2"/></svg></div>
  </article>
  <article class="card" style="left:281px">
    <div class="ph" role="img" aria-label="Illustration of a solar-roofed house connected to an underground battery" style="background:linear-gradient(180deg,#dfe3e0 0%,#3f7a32 50%,#8a6a4a 100%)"></div>
    <h4>Energy Storage Solutions</h4>
    <p>Lorem ipsum dolor sit amet consectetur. Tortor nec sed duis tristique ante massa neque. Eget lacus est volutpat velit quam cursus non enim. Elementum tempus ultrices cursus risus sit.</p>
    <div class="more">Learn More <svg width="7" height="5" viewBox="0 0 7 5" fill="none" stroke="var(--green)" stroke-width=".7"><path d="M0 2.5h6M4 .5l2 2-2 2"/></svg></div>
  </article>
  <div class="btn" style="left:176px;top:780px;width:80px;height:23px;font-size:7px">More Services</div>

  <div class="contact-band" style="top:858px;height:282px"></div>
  <h2 class="section-title abs" style="left:37px;top:913px">Get in Touch</h2>
  <p class="abs" style="left:37px;top:940px;width:152px;font-size:7px;color:#333">Lorem ipsum dolor sit amet consectetur. Tortor nec sed duis tristique ante massa neque. Eget lacus est volutpat velit quam cursus non enim. Elementum tempus ultrices cursus risus sit.</p>
  <div class="contact-line" style="left:37px;top:1006px"><svg width="11" height="8" viewBox="0 0 11 8" fill="none" stroke="#333" stroke-width=".7"><rect x=".4" y=".4" width="10.2" height="7.2"/><path d="M.4.4l5.1 4 5.1-4"/></svg>info@brightvx.com</div>
  <div class="contact-line" style="left:37px;top:1027px"><svg width="11" height="11" viewBox="0 0 11 11" fill="none" stroke="#333" stroke-width=".7"><path d="M2 1l2 2.5-1 1.3a6 6 0 003.2 3.2l1.3-1L10 9l-1.3 1.5C4.5 10 1 6.5.5 2.3z"/></svg>+43 676 0004811</div>
  <div class="contact-line" style="left:37px;top:1049px"><svg width="10" height="12" viewBox="0 0 10 12" fill="none" stroke="#333" stroke-width=".8"><path d="M5 11.5S1 7.5 1 4.8a4 4 0 018 0C9 7.5 5 11.5 5 11.5z"/><circle cx="5" cy="4.8" r="1.5"/></svg>your address here</div>

  <div class="form-card" style="left:203px;top:880px;width:191px;height:230px;padding:10px 12px">
    <h4>Contact Us</h4>
    <p style="font-size:4.8px;margin:7px 0 9px">Lorem ipsum dolor sit amet, consectetur adipiscing elit.</p>
    <div class="label">Name</div><div class="field"></div>
    <div class="label">Email</div><div class="field"></div>
    <div class="label">Message</div><div class="field msg">Type your message...</div>
    <div class="check"><i></i>I accept the <u>Terms</u></div>
    <div class="submit">Submit</div>
  </div>
</section>

<!-- ============ RIGHT PAGE ============ -->
<section class="page page-right">
  <div class="contact-band" style="top:0;height:194px;background:linear-gradient(180deg,#c9d9bf 0%,#7ab85f 100%)"></div>
  <p class="abs" style="left:37px;top:3px;width:152px;font-size:7px;color:#333">Tortor nec sed duis tristique ante massa neque. Eget lacus est volutpat velit quam cursus non enim. Elementum tempus ultrices cursus risus sit.</p>
  <div class="contact-line" style="left:37px;top:61px"><svg width="11" height="8" viewBox="0 0 11 8" fill="none" stroke="#333" stroke-width=".7"><rect x=".4" y=".4" width="10.2" height="7.2"/><path d="M.4.4l5.1 4 5.1-4"/></svg>info@brightvx.com</div>
  <div class="contact-line" style="left:37px;top:82px"><svg width="11" height="11" viewBox="0 0 11 11" fill="none" stroke="#333" stroke-width=".7"><path d="M2 1l2 2.5-1 1.3a6 6 0 003.2 3.2l1.3-1L10 9l-1.3 1.5C4.5 10 1 6.5.5 2.3z"/></svg>+43 676 0004811</div>
  <div class="contact-line" style="left:37px;top:104px"><svg width="10" height="12" viewBox="0 0 10 12" fill="none" stroke="#333" stroke-width=".8"><path d="M5 11.5S1 7.5 1 4.8a4 4 0 018 0C9 7.5 5 11.5 5 11.5z"/><circle cx="5" cy="4.8" r="1.5"/></svg>your address here</div>
  <div class="form-card" style="left:203px;top:-10px;width:191px;height:174px;padding:0 12px">
    <div class="field" style="height:12px;border-top:none"></div>
    <div class="label">Email</div><div class="field"></div>
    <div class="label">Message</div><div class="field msg">Type your message...</div>
    <div class="check"><i></i>I accept the <u>Terms</u></div>
    <div class="submit">Submit</div>
  </div>

  <div class="why-photo" role="img" aria-label="Illustration of a floating island of soil with wind turbines, solar panels and a tree"></div>
  <h2 class="section-title abs" style="left:222px;top:246px;width:190px">Why Choose BrightVX for Your Renewable Energy Needs?</h2>
  <ul class="tick-list">
    <li><svg width="9" height="9" viewBox="0 0 9 9"><circle cx="4.5" cy="4.5" r="4.5" fill="var(--green)"/><path d="M2.3 4.6l1.5 1.5 2.9-3" stroke="#fff" stroke-width=".9" fill="none"/></svg>Industry-Leading Expertise</li>
    <li><svg width="9" height="9" viewBox="0 0 9 9"><circle cx="4.5" cy="4.5" r="4.5" fill="var(--green)"/><path d="M2.3 4.6l1.5 1.5 2.9-3" stroke="#fff" stroke-width=".9" fill="none"/></svg>Customized Renewable Energy Solutions</li>
    <li style="align-items:center"><svg width="9" height="9" viewBox="0 0 9 9"><circle cx="4.5" cy="4.5" r="4.5" fill="var(--green)"/><path d="M2.3 4.6l1.5 1.5 2.9-3" stroke="#fff" stroke-width=".9" fill="none"/></svg><span style="width:180px">Commitment to Sustainability and Environmental Stewardship</span></li>
    <li><svg width="9" height="9" viewBox="0 0 9 9"><circle cx="4.5" cy="4.5" r="4.5" fill="var(--green)"/><path d="M2.3 4.6l1.5 1.5 2.9-3" stroke="#fff" stroke-width=".9" fill="none"/></svg>Exceptional Customer Service and Support:</li>
  </ul>
  <div class="btn" style="left:222px;top:396px;width:69px;height:24px;font-size:7px">Learn More</div>
  <div class="btn btn-outline" style="left:300px;top:396px;width:71px;height:24px;font-size:7px">Get Started</div>

  <div class="abs" style="left:0;top:470px;width:432px;height:198px;background:var(--mint-2)"></div>
  <h2 class="section-title abs center" style="left:0;top:499px;width:432px">What say our Clients about Us</h2>

  <div class="tcard" style="left:-55px">
    <p>Lorem ipsum dolor sit amet consectetur. Diam purus lectus nisl nisi vivamus. Tincidunt duis tellus volutpat pretium laoreet nisl platea sodales. Mi congue risus integer pharetra id. Odio quam quam massa et duis morbi egestas metus.</p>
    <div class="who"><div class="avatar" role="img" aria-label="Client portrait"></div><div><b>Orin Halvorsk</b><span>Team player</span></div></div>
    <div class="stars" style="border:.5px solid #ddd"><svg width="44" height="7" viewBox="0 0 44 7" fill="#f5c400"><g id="st"><path d="M3.5 0l1 2.3 2.5.2-1.9 1.6.6 2.4-2.2-1.3-2.2 1.3.6-2.4L0 2.5l2.5-.2z"/></g><use href="#st" x="9"/><use href="#st" x="18"/><use href="#st" x="27"/><use href="#st" x="36"/></svg></div>
  </div>
  <div class="tcard active" style="left:129px">
    <p>Lorem ipsum dolor sit amet consectetur. Diam purus lectus nisl nisi vivamus. Tincidunt duis tellus volutpat pretium laoreet nisl platea sodales. Mi congue risus integer pharetra id. Odio quam quam massa et duis morbi egestas metus.</p>
    <div class="who"><div class="avatar" style="background:#5b4a3f" role="img" aria-label="Client portrait"></div><div><b>Miles Arden</b><span>Home Owner</span></div></div>
    <div class="stars"><svg width="44" height="7" viewBox="0 0 44 7" fill="#f5c400"><use href="#st"/><use href="#st" x="9"/><use href="#st" x="18"/><use href="#st" x="27"/><use href="#st" x="36"/></svg></div>
  </div>
  <div class="tcard" style="left:311px">
    <p>Lorem ipsum dolor sit amet consectetur. Diam purus lectus nisl nisi vivamus. Tincidunt duis tellus volutpat pretium laoreet nisl platea sodales. Mi congue risus integer pharetra id. Odio quam quam massa et duis morbi egestas metus.</p>
    <div class="who"><div class="avatar" style="background:#9a8677" role="img" aria-label="Client portrait"></div><div><b>Tessa Morrow</b><span>Owner at Housing</span></div></div>
    <div class="stars" style="border:.5px solid #ddd"><svg width="44" height="7" viewBox="0 0 44 7" fill="#f5c400"><use href="#st"/><use href="#st" x="9"/><use href="#st" x="18"/><use href="#st" x="27"/><use href="#st" x="36"/></svg></div>
  </div>
  <svg class="abs" style="left:206px;top:628px" width="24" height="10" viewBox="0 0 24 10" fill="none" stroke="#333" stroke-width=".6"><circle cx="5" cy="5" r="4.5"/><path d="M5.8 3L4 5l1.8 2"/><circle cx="19" cy="5" r="4.5"/><path d="M18.2 3L20 5l-1.8 2"/></svg>

  <h2 class="section-title abs center" style="left:0;top:698px;width:432px">FAQS</h2>
  <div class="faq" style="top:751px;height:87px;background:var(--lav);padding-top:14px">
    <div class="num">01</div>
    <div style="flex:1">
      <h5>What types of renewable energy solutions does BrightVX offer?</h5>
      <p style="font-size:5.6px;color:#555;margin-top:8px;line-height:8.4px;padding-right:6px">At BrightVX, we offer a wide range of renewable energy solutions, including solar energy systems, wind turbines, and energy storage solutions. Our customized solutions are tailored to meet the specific energy requirements of your home or business."</p>
    </div>
    <div class="tog" style="background:#111;color:#fff;margin-top:2px">×</div>
  </div>
  <div class="faq" style="top:838px;height:49px;background:var(--lav-2);align-items:center"><div class="num">02</div><h5>How does the installation process work?</h5><div class="tog">+</div></div>
  <div class="faq" style="top:887px;height:54px;background:var(--lav-2);align-items:center"><div class="num">03</div><h5>What are the benefits of switching to renewable energy with BrightVX?</h5><div class="tog">+</div></div>
  <div class="faq" style="top:941px;height:56px;background:var(--lav-2);align-items:center"><div class="num">04</div><h5>How can I monitor and manage my renewable energy system?</h5><div class="tog">+</div></div>

  <footer class="footer">
    <div class="brand abs" style="left:57px;top:24px;color:#fff">BrightVX</div>
    <div class="fcol" style="left:140px"><h6>QUICK LINKS</h6><ul><li>Home</li><li>About Us</li><li>Services</li><li>Support</li><li>Contact Us</li></ul></div>
    <div class="fcol" style="left:194px;width:64px"><h6>CONTACT</h6><ul><li>BRIGHTVX ENERGY</li><li>Mail : contact@brightvx.com</li><li>Cell : +61 000 000 000</li><li>Addresse: your address, 2750 road no, city name</li></ul></div>
    <div class="fcol" style="left:279px"><h6>HELPS</h6><ul><li>Contact us</li><li>Chat with us</li><li>QA</li></ul></div>
    <div class="fcol" style="left:334px"><h6>MEET US ONLINE</h6><ul><li><i></i>Folkspace</li><li><i></i>Pictora</li><li><i></i>Zed</li><li><i></i>Workring</li><li><i></i>Clipstream</li></ul></div>
    <div class="abs" style="left:89px;top:106px;width:298px;height:.5px;background:#777"></div>
    <div class="abs" style="left:89px;top:114px;font-size:3.6px;display:flex;gap:6px"><span>Privacy Policy</span><span>Terms of Service</span><span>Cookies Settings</span></div>
    <div class="abs" style="right:45px;top:114px;font-size:3.6px">© 2024 BrightVX. All rights reserved.</div>
  </footer>
</section>

</body>
</html>
```